A website for Veltranor Limited

We need a new and modern website for our company. We are engineering consultants and contractors (EPC) in the oil and gas industry and building services industry.
What we do:
Engineering, procurement, construction
Automation (safety and process)
Non-destructive testing
Training
We have an existing website and the content can be referred from there since we are remaking the website
For more information visit Veltranor Limited Kenya

```html
<!DOCTYPE html>
<html lang="en">
<head>
<meta charset="utf-8">
<title>Veltranor Limited</title>
<link rel="stylesheet" href="https://fonts.googleapis.com/css2?family=Poppins:wght@400;500;600;700;800;900&display=swap">
<style>
:root{
  --orange:#e8582a;
  --orange-light:#f4a35a;
  --ink:#222222;
  --dark:#2d2d2d;
  --text:#444444;
  --muted:#6b6b6b;
  --light:#efefef;
  --white:#ffffff;
}
*{margin:0;padding:0;box-sizing:border-box}
html,body{width:1200px;height:4190px;overflow:hidden;background:var(--white)}
body{position:relative;font-family:'Poppins',sans-serif;color:var(--text)}
.abs{position:absolute}
.brand{display:flex;align-items:center;gap:12px}
.brand-dot{width:56px;height:56px;border-radius:50%;border:3px solid var(--orange)}
.brand-name{font-family:'Poppins',sans-serif;font-weight:400;color:var(--orange);font-size:26px;line-height:1.15;text-transform:uppercase;letter-spacing:1px}

/* header */
.logo-panel{left:0;top:0;width:392px;height:133px;background:var(--light);clip-path:polygon(0 0,340px 0,392px 66px,340px 133px,0 133px)}
.topbar{left:340px;top:0;width:860px;height:33px;background:var(--ink);clip-path:polygon(0 0,100% 0,100% 100%,26px 100%)}
.topbar-text{left:376px;top:9px;font-size:12px;color:var(--white);font-weight:500}
.topbar-social{right:30px;top:12px;display:flex;gap:11px}
.topbar-social span{width:9px;height:9px;border-radius:50%;background:var(--white)}
.contact-item{top:48px;display:flex;gap:10px;align-items:flex-start;font-size:12.5px;color:var(--ink);font-weight:500;line-height:1.35}
.contact-item b{font-weight:700}
.nav-band{left:550px;top:98px;width:650px;height:58px;background:linear-gradient(90deg,var(--orange),var(--orange-light));clip-path:polygon(30px 0,100% 0,100% 100%,0 100%)}
.nav{left:622px;top:120px;display:flex;gap:24px;font-size:12px;font-weight:600;color:var(--white);text-transform:uppercase}

/* hero */
.hero{left:0;top:133px;width:1200px;height:772px;background:linear-gradient(110deg,#1c1c1c 0%,#2e2a26 40%,#6a5033 70%,#c07a2f 100%);clip-path:polygon(0 0,100% 0,100% 688px,0 100%)}
.hero-title{left:88px;top:330px;font-size:76px;font-weight:900;line-height:.94;color:var(--white);text-transform:uppercase;letter-spacing:-1px}
.hero-sub{left:88px;top:564px;font-size:18px;font-weight:700;line-height:1.5;color:var(--white);text-transform:uppercase}
.btn-light{left:88px;top:642px;width:190px;height:49px;background:var(--white);clip-path:polygon(0 0,100% 0,88% 100%,0 100%);display:flex;align-items:center;padding-left:30px;gap:14px;font-size:13px;font-weight:700;color:var(--ink);text-transform:uppercase}
.hero-marker{left:572px;top:821px}

/* section titles */
.section-title{font-size:32px;font-weight:800;color:var(--ink);text-transform:uppercase}

/* about */
.about-photo{left:90px;top:870px;width:560px;height:495px;background:radial-gradient(ellipse at 55% 45%,#c98a4a 0%,#9a8f86 35%,#d9d9d9 70%,rgba(255,255,255,0) 100%)}
.about-title{left:720px;top:978px}
.about-rule{left:700px;top:1020px;width:68px;height:2px;background:#cccccc}
.about-text{left:720px;top:1032px;width:370px;font-size:14.5px;line-height:1.36;color:var(--text)}
.about-text p+p{margin-top:20px}
.btn-outline{left:720px;top:1228px;width:180px;height:46px;display:flex;align-items:center;padding-left:36px;gap:14px;font-size:13px;font-weight:700;color:var(--ink);text-transform:uppercase}
.btn-outline svg{position:absolute;left:0;top:0}

/* services */
.services-title{left:0;top:1425px;width:1200px;text-align:center}
.service-card{top:1491px;width:249px;height:403px;background:var(--white);box-shadow:0 14px 22px rgba(0,0,0,.12);clip-path:polygon(0 0,100% 0,100% 94%,0 100%)}
.service-photo{height:220px}
.service-name{margin:30px 0 0 27px;font-size:16px;font-weight:700;color:var(--ink);text-transform:uppercase}
.service-text{margin:8px 27px 0;font-size:12.5px;line-height:1.55;color:var(--text)}
.service-more{margin:12px 0 0 27px;font-size:11px;font-weight:700;color:var(--orange);text-transform:uppercase;text-decoration:underline}
.arrow-btn{width:41px;height:38px;display:flex;align-items:center;justify-content:center}
.arrow-btn.light{background:#dedede}
.arrow-btn.dark{background:var(--ink)}

/* video */
.video{left:0;top:2065px;width:1200px;height:642px;background:linear-gradient(100deg,#8c8a80 0%,#c9873e 35%,#b46a2f 60%,#3e3f45 100%);clip-path:polygon(0 0,100% 0,100% 100%,0 463px)}
.video-word{left:0;top:2215px;width:1200px;text-align:center;font-size:190px;font-weight:900;color:var(--white);letter-spacing:-6px;line-height:1}
.play{left:748px;top:2272px}

/* work */
.work-ring{left:36px;top:2756px}
.work-title{left:155px;top:2880px}
.work-text{left:155px;top:2940px;width:230px;font-size:14px;line-height:1.4;color:var(--text)}
.work-grid{left:420px;top:2750px;display:grid;grid-template-columns:repeat(3,211px);grid-template-rows:repeat(2,211px);gap:6px}

/* testimonials */
.testi-photo{left:98px;top:3252px;width:528px;height:553px;background:radial-gradient(ellipse at 45% 55%,#c0814e 0%,#a26a4c 30%,#d8c8b8 60%,rgba(255,255,255,0) 80%)}
.quote-mark{left:645px;top:3230px;font-size:260px;font-weight:900;color:#ececec;line-height:1}
.testi-title{left:699px;top:3360px}
.testi-text{left:706px;top:3409px;width:410px;font-size:15px;line-height:1.45;color:var(--text)}
.testi-name{left:706px;top:3548px;font-size:14px;font-weight:700;color:var(--ink);text-transform:uppercase}
.stars{left:706px;top:3568px;font-size:15px;letter-spacing:3px;color:#f39a2a}

/* footer */
.footer{left:0;top:3715px;width:1200px;height:475px;background:var(--dark);clip-path:polygon(0 109px,100% 0,100% 100%,0 100%)}
.footer-brand{left:150px;top:3925px}
.footer-brand .brand-dot{width:66px;height:66px;border-color:var(--white)}
.footer-brand .brand-name{color:var(--white);font-size:28px}
.footer-social{left:236px;top:4015px;display:flex;gap:10px}
.footer-social span{width:33px;height:33px;border-radius:50%;border:1px solid #555;background:#3a3a3a}
.footer-col{top:3880px;color:var(--white)}
.footer-col h4{font-size:14px;font-weight:700;text-transform:uppercase;margin-bottom:14px}
.footer-col li{list-style:none;font-size:12.5px;line-height:24.4px;color:#dddddd}
.contact-row{display:flex;gap:8px;font-size:12.5px;line-height:1.35;color:#dddddd;margin-bottom:10px;width:240px}
.contact-row svg{flex:none;margin-top:3px}
.footer-rule{left:90px;top:4130px;width:1020px;height:1px;background:#4a4a4a}
.copyright{left:0;top:4152px;width:1200px;text-align:center;font-size:11px;font-weight:500;color:var(--white);text-transform:uppercase}
.to-top{left:1134px;top:4112px;width:40px;height:40px;border-radius:50%;background:var(--orange);display:flex;align-items:center;justify-content:center}
</style>
</head>
<body>

<!-- header -->
<div class="abs logo-panel"></div>
<div class="abs brand" style="left:58px;top:22px">
  <span class="brand-dot"></span>
  <span class="brand-name">Veltranor<br>Limited</span>
</div>
<div class="abs topbar"></div>
<div class="abs topbar-text">Your Trusted 24 Hours Construction Service Provider!</div>
<div class="abs topbar-social"><span></span><span></span><span></span><span></span></div>

<div class="abs contact-item" style="left:720px">
  <svg width="20" height="20" viewBox="0 0 24 24"><path fill="#222" d="M6.6 10.8a15 15 0 0 0 6.6 6.6l2.2-2.2c.3-.3.7-.4 1-.2 1.1.4 2.3.6 3.6.6.6 0 1 .4 1 1V20c0 .6-.4 1-1 1A17 17 0 0 1 3 4c0-.6.4-1 1-1h3.5c.6 0 1 .4 1 1 0 1.3.2 2.5.6 3.6.1.3 0 .7-.2 1z"/></svg>
  <div>Call Us<br><b>+254 700 410 262</b></div>
</div>
<div class="abs" style="left:885px;top:50px;width:1px;height:34px;background:#dddddd"></div>
<div class="abs contact-item" style="left:927px">
  <svg width="18" height="18" viewBox="0 0 24 24"><path fill="#222" d="M2 5h20v14H2zm2 2v.5l8 5 8-5V7l-8 5z"/></svg>
  <div>Email<br><b>info@veltranor.example</b></div>
</div>

<div class="abs nav-band"></div>
<nav class="abs nav"><span>Home</span><span>About Us</span><span>What We Do</span><span>Projects</span><span>Services</span><span>Contact</span></nav>

<!-- hero -->
<div class="abs hero" role="img" aria-label="Photo of two engineers in hard hats and safety vests reviewing a laptop"></div>
<h1 class="abs hero-title">We Create<br>Space For<br>Life</h1>
<p class="abs hero-sub">Veltranor' core business is engineering<br>works (Oil and Gas Engineering)</p>
<div class="abs btn-light">Contact Us
  <svg width="14" height="10" viewBox="0 0 14 10"><path d="M0 5h12M8 1l4 4-4 4" stroke="#222" stroke-width="1.4" fill="none"/></svg>
</div>
<svg class="abs hero-marker" width="56" height="66" viewBox="0 0 56 66"><path d="M0 0h56L28 66z" fill="#2d2d2d"/><path d="M22 16l6 6 6-6" stroke="#fff" stroke-width="2" fill="none"/></svg>

<!-- about -->
<div class="abs about-photo" role="img" aria-label="Double exposure of a worker with hard hat and blueprints blended with a city skyline"></div>
<h2 class="abs section-title about-title">About Veltranor</h2>
<div class="abs about-rule"></div>
<div class="abs about-text">
  <p>Veltranor undertakes Design, Supply, Installation and Commissioning of LPG and Petroleum systems including LPG Reticulated Systems (piped gas). We also do LPG tank revalidation and recertification.</p>
  <p>Our clients include: Oil companies (both multinationals and local), government agencies, manufacturing companies, agricultural institutions, and the building services industry.</p>
</div>
<div class="abs btn-outline">
  <svg width="180" height="46" viewBox="0 0 180 46"><path d="M1 1h178l-22 44H1z" stroke="#222" stroke-width="1.5" fill="none"/></svg>
  <span style="position:relative">Read More</span>
  <svg style="position:relative" width="14" height="10" viewBox="0 0 14 10"><path d="M0 5h12M8 1l4 4-4 4" stroke="#222" stroke-width="1.4" fill="none"/></svg>
</div>

<!-- services -->
<h2 class="abs section-title services-title">Our Services</h2>
<article class="abs service-card" style="left:88px">
  <div class="service-photo" role="img" aria-label="Engineer operating machinery in a workshop" style="background:linear-gradient(135deg,#5a5e62,#9a8a78 60%,#d07a2e)"></div>
  <h3 class="service-name">Engineering</h3>
  <p class="service-text">Lorem Ipsum is simply dummy text of the printing typesetting industry lorem Ipsum has...</p>
  <div class="service-more">Read More</div>
</article>
<article class="abs service-card" style="left:346px">
  <div class="service-photo" role="img" aria-label="Two engineers reviewing documents in a warehouse" style="background:linear-gradient(135deg,#7d8a96,#b0b6bb 55%,#c8a040)"></div>
  <h3 class="service-name">Procurement</h3>
  <p class="service-text">Lorem Ipsum is simply dummy text of the printing typesetting industry lorem Ipsum has...</p>
  <div class="service-more">Read More</div>
</article>
<article class="abs service-card" style="left:603px">
  <div class="service-photo" role="img" aria-label="Construction workers in orange vests shaking hands" style="background:linear-gradient(135deg,#7a6a5a,#d46a2a 55%,#e0a040)"></div>
  <h3 class="service-name">Construction</h3>
  <p class="service-text">Lorem Ipsum is simply dummy text of the printing typesetting industry lorem Ipsum has...</p>
  <div class="service-more">Read More</div>
</article>
<article class="abs service-card" style="left:862px">
  <div class="service-photo" role="img" aria-label="Engineer with a tablet beside an industrial robot arm" style="background:linear-gradient(135deg,#3e4a58,#6c7a88 55%,#d8b030)"></div>
  <h3 class="service-name">Automation</h3>
  <p class="service-text">Lorem Ipsum is simply dummy text of the printing typesetting industry lorem Ipsum has...</p>
  <div class="service-more">Read More</div>
</article>
<div class="abs arrow-btn light" style="left:556px;top:1943px"><svg width="10" height="10" viewBox="0 0 10 10"><path d="M6.5 1.5L3 5l3.5 3.5" stroke="#222" stroke-width="1.6" fill="none"/></svg></div>
<div class="abs arrow-btn dark" style="left:603px;top:1943px"><svg width="10" height="10" viewBox="0 0 10 10"><path d="M3.5 1.5L7 5 3.5 8.5" stroke="#fff" stroke-width="1.6" fill="none"/></svg></div>

<!-- video -->
<div class="abs video" role="img" aria-label="Video still of construction workers in hard hats discussing plans at a table"></div>
<div class="abs video-word">VIDEO</div>
<svg class="abs play" width="130" height="130" viewBox="0 0 130 130"><circle cx="65" cy="65" r="65" fill="#fff"/><path d="M58 54l16 11-16 11z" fill="#222"/></svg>

<!-- work -->
<svg class="abs work-ring" width="410" height="410" viewBox="0 0 410 410">
  <defs><linearGradient id="ringGrad" x1="0" y1="0" x2="1" y2="1"><stop offset="0" stop-color="#e8582a"/><stop offset="1" stop-color="#f4a35a"/></linearGradient></defs>
  <circle cx="205" cy="205" r="202" fill="none" stroke="url(#ringGrad)" stroke-width="4"/>
</svg>
<h2 class="abs section-title work-title">Our Work</h2>
<p class="abs work-text">Veltranor' core business is engineering works (Oil and Gas Engineering).</p>
<div class="abs arrow-btn light" style="left:155px;top:3021px;width:38px;height:36px"><svg width="10" height="10" viewBox="0 0 10 10"><path d="M6.5 1.5L3 5l3.5 3.5" stroke="#222" stroke-width="1.6" fill="none"/></svg></div>
<div class="abs arrow-btn dark" style="left:204px;top:3021px;width:38px;height:36px"><svg width="10" height="10" viewBox="0 0 10 10"><path d="M3.5 1.5L7 5 3.5 8.5" stroke="#fff" stroke-width="1.6" fill="none"/></svg></div>
<div class="abs work-grid">
  <div role="img" aria-label="Worker with hard hat and tool belt" style="background:linear-gradient(135deg,#8a5a4a,#d8a040 60%,#c09070)"></div>
  <div role="img" aria-label="Team reviewing building plans on site" style="background:linear-gradient(135deg,#c8ccd0,#8a8c90 50%,#d46a2a)"></div>
  <div role="img" aria-label="Workers welding with sparks" style="background:linear-gradient(135deg,#9aa4ae,#d86a2a 55%,#3a4a6a)"></div>
  <div role="img" aria-label="Workers in safety vests on a site" style="background:linear-gradient(135deg,#5a5048,#d8702a 50%,#9ab040)"></div>
  <div role="img" aria-label="Engineer in hard hat with a laptop" style="background:linear-gradient(135deg,#3a3e44,#7a8088 55%,#d8d8d8)"></div>
  <div role="img" aria-label="Builders reviewing plans beside high-rise blocks" style="background:linear-gradient(135deg,#8a7a6a,#e08a3a 55%,#c8c0b0)"></div>
</div>

<!-- testimonials -->
<div class="abs testi-photo" role="img" aria-label="Double exposure of a worker in a hard hat holding plans blended with a city at sunset"></div>
<div class="abs quote-mark">“</div>
<h2 class="abs section-title testi-title">Testimonials</h2>
<p class="abs testi-text">Lorem Ipsum is simply dummy text of the printing and typesetting industry. Lorem Ipsum has been the industry's standard dummy text ever since the 1500s, when an unknown printer took a galley of type and scrambled it to make a type specimen book.</p>
<div class="abs testi-name">Daniel Marwa</div>
<div class="abs stars">★★★★★</div>
<div class="abs arrow-btn light" style="left:706px;top:3601px;width:40px"><svg width="10" height="10" viewBox="0 0 10 10"><path d="M6.5 1.5L3 5l3.5 3.5" stroke="#222" stroke-width="1.6" fill="none"/></svg></div>
<div class="abs arrow-btn dark" style="left:754px;top:3601px;width:40px"><svg width="10" height="10" viewBox="0 0 10 10"><path d="M3.5 1.5L7 5 3.5 8.5" stroke="#fff" stroke-width="1.6" fill="none"/></svg></div>

<!-- footer -->
<footer>
  <div class="abs footer"></div>
  <div class="abs brand footer-brand">
    <span class="brand-dot"></span>
    <span class="brand-name">Veltranor<br>Limited</span>
  </div>
  <div class="abs footer-social"><span></span><span></span><span></span></div>

  <div class="abs footer-col" style="left:470px">
    <h4>Useful Links</h4>
    <ul><li>Home</li><li>About Us</li><li>What we do</li><li>Projects</li><li>Services</li><li>Contact</li></ul>
  </div>
  <div class="abs footer-col" style="left:639px">
    <h4>Our Services</h4>
    <ul><li>Engineering</li><li>Procurement</li><li>Construction</li><li>Automation</li><li>Non-destructive testing</li><li>Training</li></ul>
  </div>
  <div class="abs footer-col" style="left:836px">
    <h4>Contact Us</h4>
    <div class="contact-row">
      <svg width="10" height="13" viewBox="0 0 10 13"><path d="M5 0a5 5 0 0 1 5 5c0 3.5-5 8-5 8S0 8.5 0 5a5 5 0 0 1 5-5zm0 3a2 2 0 1 0 0 4 2 2 0 0 0 0-4z" fill="#e8582a"/></svg>
      <span>Kestrel House, Next to Harbor Plaza, Ridgeway, Suite 14, Coast Road</span>
    </div>
    <div class="contact-row">
      <svg width="11" height="11" viewBox="0 0 24 24"><path fill="#e8582a" d="M6.6 10.8a15 15 0 0 0 6.6 6.6l2.2-2.2c.3-.3.7-.4 1-.2 1.1.4 2.3.6 3.6.6.6 0 1 .4 1 1V20c0 .6-.4 1-1 1A17 17 0 0 1 3 4c0-.6.4-1 1-1h3.5c.6 0 1 .4 1 1 0 1.3.2 2.5.6 3.6.1.3 0 .7-.2 1z"/></svg>
      <span>Cell:<br>+254 711 305 748, +254 700 410 262</span>
    </div>
    <div class="contact-row">
      <svg width="11" height="11" viewBox="0 0 24 24"><path fill="#e8582a" d="M2 5h20v14H2zm2 2v.5l8 5 8-5V7l-8 5z"/></svg>
      <span>Email:<br>info@veltranor.example</span>
    </div>
  </div>

  <div class="abs footer-rule"></div>
  <div class="abs copyright">Copyright © 2023 Veltranor. All rights reserved.</div>
  <div class="abs to-top"><svg width="12" height="12" viewBox="0 0 12 12"><path d="M2 8l4-4 4 4" stroke="#fff" stroke-width="1.8" fill="none"/></svg></div>
</footer>

</body>
</html>
```